Redesign of Website

We need an overhaul of our website. I've attached our current logo files. Please visit www.qelvorbis.com for our current website for information about our company. We are looking for the same type of website (information-based only) so no need for any online store, payments, interactive stuff or anything like that...basically looking for a fresh new look! Also please make sure this design will be mobile-friendly. Thanks!

```html
<!DOCTYPE html>
<html lang="en">
<head>
<meta charset="utf-8">
<title>Qelvorbis Consultants, Inc.</title>
<link href="https://fonts.googleapis.com/css2?family=Montserrat:wght@400;500;600;700&display=swap" rel="stylesheet">
<style>
:root{
  --navy:#10254a;
  --blue:#2a7bc0;
  --ink:#1c2b45;
  --muted:#8a93a3;
  --pale:#eef2f6;
  --white:#ffffff;
}
*{margin:0;padding:0;box-sizing:border-box}
html,body{width:1200px;height:2961px;overflow:hidden;background:var(--white)}
body{position:relative;font-family:'Montserrat',sans-serif;color:var(--ink)}
.abs{position:absolute}
.btn-solid{position:absolute;background:var(--blue);color:#fff;border-radius:18px;font-size:12px;font-weight:500;display:flex;align-items:center;justify-content:center}
.btn-line{position:absolute;border:2px solid var(--blue);color:var(--blue);border-radius:18px;font-size:12px;font-weight:500;display:flex;align-items:center;justify-content:center;background:transparent}
/* header */
.site-header{position:absolute;left:0;top:0;width:1200px;height:79px;background:#fff;z-index:3}
.brand{position:absolute;left:59px;top:22px;display:flex;align-items:center;gap:10px;color:var(--navy);font-size:22px;font-weight:600}
.brand-dot{width:26px;height:26px;background:var(--navy);border-radius:50%}
.nav a{position:absolute;top:32px;font-size:12px;color:var(--ink);text-decoration:none}
.nav a.active{color:var(--blue)}
.call{position:absolute;left:762px;top:22px}
.call-label{position:absolute;left:43px;top:2px;font-size:11px;white-space:nowrap}
.call-num{position:absolute;left:43px;top:16px;font-size:16px;font-weight:600;color:var(--blue);white-space:nowrap}
.quote-tab{position:absolute;left:961px;top:0;width:239px;height:79px;background:var(--blue);color:#fff;font-size:15px;display:flex;align-items:center;justify-content:center}
/* hero */
.hero{position:absolute;left:0;top:79px;width:1200px;height:513px}
.hero-title{position:absolute;left:0;width:1200px;text-align:center;color:#fff}
.dots{position:absolute;left:1011px;top:304px}
.dots span{display:block;width:12px;height:12px;border:2px solid #fff;border-radius:50%;margin-bottom:7px}
.dots span.on{background:#fff}
/* services */
.section-title{position:absolute;left:0;width:1200px;text-align:center;font-weight:600;color:var(--navy)}
.card{position:absolute;top:720px;width:240px}
.card-img{width:240px;height:160px}
.card h3{margin-top:30px;font-size:14px;font-weight:600;line-height:20px;color:var(--navy)}
.card p{margin-top:6px;font-size:11.5px;line-height:17px;color:var(--muted)}
.card .btn-line{position:static;width:81px;height:32px;margin-top:24px}
.slide-arrow{position:absolute;width:20px;height:20px;border:1.5px solid var(--muted);border-radius:50%}
/* team */
.member{position:absolute;top:2150px;width:174px;text-align:center}
.avatar{width:174px;height:174px;border-radius:50%}
.member h4{margin-top:24px;font-size:15px;font-weight:500;color:var(--blue)}
.member span{display:block;font-size:10px;color:var(--muted);margin-top:2px}
/* footer */
.field{position:absolute;border:1px solid #6b7d9c;color:#c7d0de;font-size:11px;padding:0 14px;display:flex;align-items:center}
.social{position:absolute;top:2803px;width:30px;height:30px;border:1.5px solid #6b7d9c;border-radius:50%}
.bottom-bar{position:absolute;left:0;top:2898px;width:1200px;height:63px;background:#eef1f5;font-size:10px;color:var(--ink)}
</style>
</head>
<body>

<header class="site-header">
  <div class="brand"><span class="brand-dot"></span>Qelvorbis Consultants, Inc.</div>
  <nav class="nav">
    <a class="active" style="left:357px">Home</a>
    <a style="left:426px">About</a>
    <a style="left:497px">Services</a>
    <a style="left:578px">Contact</a>
  </nav>
  <div class="call">
    <svg width="34" height="34" viewBox="0 0 34 34"><circle cx="17" cy="17" r="15" fill="none" stroke="#2a7bc0" stroke-width="2"/><path d="M12 10c1-1 2 0 3 2s0 2-1 3c1 2 3 4 5 5 1-1 2-2 3-1s3 2 2 3c-1 2-3 2-5 1-3-2-6-5-8-8-1-2-1-4 1-5z" fill="#2a7bc0"/></svg>
    <div class="call-label">Call Us Today!</div>
    <div class="call-num">555 - 014 - 2290</div>
  </div>
  <div class="quote-tab">Get Free Quotes!</div>
</header>

<section class="hero">
  <svg class="abs" style="left:0;top:0" width="1200" height="513" role="img" aria-label="Photo of timber house framing against a blue sky">
    <defs><linearGradient id="heroSky" x1="0" y1="0" x2="0" y2="1"><stop offset="0" stop-color="#2c4a78"/><stop offset=".55" stop-color="#6d7c86"/><stop offset="1" stop-color="#a88e66"/></linearGradient></defs>
    <polygon points="0,0 1200,0 1200,414 600,513 0,414" fill="url(#heroSky)"/>
  </svg>
  <div class="hero-title" style="top:196px;font-size:32px;font-weight:600">Over 25 Years Experience</div>
  <div class="hero-title" style="top:234px;font-size:21px;font-weight:400">Specialists In Construction and Loan Management</div>
  <div class="btn-solid" style="left:519px;top:283px;width:162px;height:35px">Contact Us Today!</div>
  <div class="dots"><span class="on"></span><span></span><span></span><span></span></div>
  <svg class="abs" style="left:591px;top:460px" width="18" height="28"><path d="M9 2v22M3 18l6 6 6-6" stroke="#fff" stroke-width="2" fill="none"/></svg>
</section>

<h2 class="section-title" style="top:656px;font-size:24px">Service We Offers</h2>
<span class="slide-arrow" style="left:154px;top:791px"></span>
<span class="slide-arrow" style="left:1025px;top:791px"></span>

<article class="card" style="left:207px">
  <div class="card-img" role="img" aria-label="Photo of a house seen through a magnifying glass" style="background:linear-gradient(160deg,#7ea3c9,#b9a58a)"></div>
  <h3>Property Condition<br>Reports</h3>
  <p>Before moving ahead on any loan approval, financial institutions need to know the condition of existing structures.</p>
  <div class="btn-line">More</div>
</article>
<article class="card" style="left:480px">
  <div class="card-img" role="img" aria-label="Photo of hands reviewing plans on a tablet" style="background:linear-gradient(160deg,#d9d6d0,#8c8a86)"></div>
  <h3>Plan and Cost<br>Reviews</h3>
  <p>Our Plan nd Cost Reviews provide lending institutions with expert analysis of new construction projects before loan commitments are ...</p>
  <div class="btn-line">More</div>
</article>
<article class="card" style="left:752px">
  <div class="card-img" role="img" aria-label="Photo of a model house on banknotes" style="background:linear-gradient(160deg,#f1efe9,#b8ab8c)"></div>
  <h3>Construction Funding<br>Inspections</h3>
  <p>Lending institutions rarely have employees with the expertise needed to evaluate multiple stages of site construction and ensure ...</p>
  <div class="btn-line">More</div>
</article>

<svg class="abs" style="left:0;top:1131px" width="1200" height="316" role="img" aria-label="Photo of engineers in front of a building under construction">
  <defs><linearGradient id="bandBg" x1="0" y1="0" x2="1" y2="0"><stop offset="0" stop-color="#4d5a63"/><stop offset=".5" stop-color="#2f4a74"/><stop offset="1" stop-color="#5d7595"/></linearGradient></defs>
  <polygon points="0,90 600,0 1200,90 1200,316 0,316" fill="url(#bandBg)"/>
</svg>
<div class="section-title" style="top:1229px;font-size:28px;color:#fff;line-height:34px">All construction projects start<br>with the foundation.</div>
<div class="section-title" style="top:1304px;font-size:14px;font-weight:400;color:#fff">Qelvorbis Consultants, Inc. do the groundwork to ensure you're building on a solid foundation.</div>
<div class="btn-solid" style="left:521px;top:1352px;width:158px;height:32px">Get Free Quotes!</div>

<svg class="abs" style="left:0;top:1447px" width="1200" height="547"><polygon points="0,0 1200,0 1200,458 600,547 0,458" fill="#eef2f6"/></svg>
<div class="abs" role="img" aria-label="Photo of two businessmen discussing documents" style="left:207px;top:1528px;width:393px;height:312px;background:linear-gradient(135deg,#2e3b52,#c9ccd0 70%,#eef0f1)"></div>
<div class="abs" style="left:638px;top:1555px;font-size:14px;font-weight:600;color:var(--navy)">QELVORBIS.com –</div>
<div class="abs" style="left:638px;top:1575px;font-size:24px;font-weight:600;color:var(--navy)">Qelvorbis Consultants, Inc.</div>
<div class="abs" style="left:638px;top:1618px;width:352px;font-size:11.5px;line-height:17px;color:var(--muted)">
  <p>With over 25 years experience we provide customized and comprehensive inspection services to financial institutions involved in construction and loan management in New York, New Jersey, Pennsylvania and surrounding areas.</p>
  <p style="margin-top:17px">The firm's professional staff bring years of engineering, environmental, building, and real estate experience to work for our clients.</p>
  <p style="margin-top:17px">Qelvorbis provides our clients with in-depth plan &amp; cost, construction funding, environmental and property condition reports.</p>
</div>
<div class="btn-line" style="left:543px;top:1889px;width:113px;height:33px">About Us</div>
<svg class="abs" style="left:580px;top:1985px" width="40" height="40"><circle cx="20" cy="20" r="19" fill="#fff"/><path d="M20 12v15M15 22l5 5 5-5" stroke="#1c2b45" stroke-width="1.5" fill="none"/></svg>

<h2 class="section-title" style="top:2068px;font-size:24px;font-weight:500">Our Team</h2>
<div class="section-title" style="top:2100px;font-size:11px;font-weight:400;color:var(--muted)">Decades of Experience in Every Phase of Construction</div>
<span class="slide-arrow" style="left:154px;top:2227px"></span>
<span class="slide-arrow" style="left:1025px;top:2227px"></span>
<div class="member" style="left:207px"><div class="avatar" role="img" aria-label="Portrait of team member" style="background:linear-gradient(160deg,#c9cfd6,#5a6474)"></div><h4>Elias Varn</h4><span>President</span></div>
<div class="member" style="left:410px"><div class="avatar" role="img" aria-label="Portrait of team member" style="background:linear-gradient(160deg,#e3e3e3,#2c3445)"></div><h4>Theo Varn</h4><span>Chief Financial Officer</span></div>
<div class="member" style="left:616px"><div class="avatar" role="img" aria-label="Portrait of team member" style="background:linear-gradient(160deg,#f2f2f2,#3a4050)"></div><h4>Nadia Korbel</h4><span>Director of Operations</span></div>
<div class="member" style="left:819px"><div class="avatar" role="img" aria-label="Portrait of team member" style="background:linear-gradient(160deg,#b7c7cc,#2b3546)"></div><h4>Owen Hartle</h4><span>Product Distribution Manager</span></div>

<svg class="abs" style="left:0;top:2440px" width="1200" height="458"><polygon points="0,97 600,0 1200,97 1200,458 0,458" fill="#10254a"/></svg>
<div class="section-title" style="top:2537px;font-size:24px;font-weight:500;color:#fff;line-height:32px">Do you have a Construction Project?<br>Contact Us Today!</div>
<div class="abs" style="left:207px;top:2628px;color:#fff;font-size:14px;font-weight:600">Qelvorbis Consultants, Inc.</div>
<div class="abs" style="left:207px;top:2650px;color:#c7d0de;font-size:11px;line-height:20px">118 Linden Ridge Rd #204<br>Marlow Township,<br>NJ 07990</div>
<div class="abs" style="left:207px;top:2725px;color:var(--blue);font-size:14px">P. 555 - 014 - 2290</div>
<div class="abs" style="left:207px;top:2746px;color:#c7d0de;font-size:11px">e. info@qelvorbis.com</div>
<span class="social" style="left:208px"></span>
<span class="social" style="left:249px"></span>
<span class="social" style="left:289px"></span>
<div class="field" style="left:480px;top:2633px;width:160px;height:32px">Enter your Name</div>
<div class="field" style="left:664px;top:2633px;width:151px;height:32px">Email</div>
<div class="field" style="left:832px;top:2633px;width:161px;height:32px">Phone</div>
<div class="field" style="left:480px;top:2681px;width:513px;height:94px;align-items:flex-start;padding-top:10px">Message ...</div>
<div class="btn-solid" style="left:480px;top:2801px;width:111px;height:32px">Submit</div>

<footer class="bottom-bar">
  <div class="abs" style="left:207px;top:26px">Copyright 2019 &nbsp;|&nbsp; QELVORBIS.com</div>
  <div class="abs" style="left:787px;top:26px"><span style="color:var(--blue)">Home</span> &nbsp;|&nbsp; About &nbsp;|&nbsp; Services &nbsp;|&nbsp; Contact</div>
  <svg class="abs" style="left:1129px;top:20px" width="18" height="24"><path d="M9 22V3M3 9l6-6 6 6" stroke="#2a7bc0" stroke-width="1.5" fill="none"/></svg>
</footer>

</body>
</html>
```